Landing Page Design for Fellas Past Fifty

I have an exercise book that I sell through Instagram. One of my teaching concepts has grow to be running joke yet valuable because it really works. It’s called the Quick Tick Quest. Its purpose is to create a habit / a daily habit of exercise by starting with just 10 seconds a day but doing it everyday for 30 days. After the habit is established the time is increased. Ten seconds is such a ridiculous amount of exercise time but help establish the habit. We need a landing page; sexy, eye catching for guys, FUN with a touch of tease. Classy not as “Tacky LasVegas” as the attached. Fellas PastFifty were born 1960 to 1975.
Change copy slightly as you see fit. We will run an Simple Instagram Ad with the headline

“ FellasPastFifty
out of shape & overweight
Discover Insanely Simple Steps
to Get You in Shape Before Your Health Deteriorates,
You Develop Diabetes,
Have a Stroke & Die Way Too Early.
Learn More

from this IG Ad they will go to the landing page. A coordinating layout of this IG ad would be nice also.
I have attached the copy for the landing page and a “Tacky” design; again I need sexy but more classy. I want to catch the attention of guys.
Thank you_Bo
PS: I need a long term relationship to make future copy adjustments and hopefully you have the ability to make the site go live with a connection to my samcart or another site for purchases. Looking forward to your design.

Target Market(s)

Men / Fellas Past Fifty

Industry/Entity Type

Health And Wellness

Number of Pages Required

1 page

Font styles to use
Sans Serif

Requirements
Must have
• A simple classy sexy design with Eye appeal to Fellas Past Fifty

I own these two websites
www.FellasPastFifty.com www.TheQuickTickQuest.com
Nice to have
• Long term relationship for this project and future projects.
I'm an entrepreneur in need of tech support.
Should not have
• Should not have Too much clutter and not be tacky

```html
<!DOCTYPE html>
<html lang="en">
<head>
<meta charset="utf-8">
<title>Quick Tick Quest – Fellas Past Fifty</title>
<link href="https://fonts.googleapis.com/css2?family=Montserrat:wght@600;700;800&family=Barlow:wght@400;500;600&display=swap" rel="stylesheet">
<style>
  :root {
    --orange: #e8620f;
    --orange-soft: #f07a2a;
    --orange-deep: #b9450a;
    --ember: #8f3408;
    --ink: #121212;
    --ink-soft: #1b1b1b;
    --line: rgba(255,255,255,.18);
    --white: #ffffff;
    --muted: #d9d4cf;
    --footer: #050505;
  }
  * { margin: 0; padding: 0; box-sizing: border-box; }
  html, body { width: 950px; height: 1200px; overflow: hidden; background: var(--ink); }
  .page { position: relative; width: 950px; height: 1200px; font-family: "Barlow", Arial, sans-serif; color: var(--white); overflow: hidden; }
  .abs { position: absolute; }
  .backdrop { position: absolute; left: 0; top: 0; width: 950px; height: 1144px; }

  .hero-photo { left: 0; top: 0; width: 475px; height: 520px;
    background: radial-gradient(ellipse at 60% 30%, rgba(255,200,150,.28), rgba(232,98,15,0) 62%); }

  .brand { left: 0; width: 950px; text-align: center; font-family: "Montserrat", Arial, sans-serif; color: var(--white); }
  .brand-main { top: 46px; font-size: 46px; font-weight: 800; letter-spacing: 4px; }
  .brand-sub { top: 110px; font-size: 22px; font-weight: 700; letter-spacing: 12px; padding-left: 12px; }
  .brand-rule { left: 445px; top: 150px; width: 60px; height: 2px; background: var(--white); }

  .col { left: 475px; width: 475px; text-align: center; }
  .eyebrow { top: 208px; font-size: 12px; font-weight: 600; letter-spacing: 4px; color: var(--muted); }
  .headline { top: 230px; font-family: "Montserrat", Arial, sans-serif; font-weight: 800; font-size: 34px; letter-spacing: 1px; color: var(--orange); }
  .subhead { top: 284px; font-family: "Montserrat", Arial, sans-serif; font-weight: 700; font-size: 18px; letter-spacing: 2px; }
  .rule { left: 682px; width: 60px; height: 2px; background: var(--orange); }
  .rule-1 { top: 324px; }
  .intro { top: 344px; left: 510px; width: 405px; text-align: center; font-size: 14.5px; line-height: 26px; color: var(--muted); }
  .goal { top: 452px; font-size: 23px; font-weight: 500; }
  .secret { top: 486px; font-size: 16px; color: var(--muted); }
  .starts { top: 560px; font-size: 20px; }
  .quest { top: 588px; font-family: "Montserrat", Arial, sans-serif; font-size: 30px; font-weight: 700; color: var(--orange); }
  .last { top: 640px; font-size: 17px; }
  .upfor { top: 670px; font-size: 17px; font-style: italic; color: var(--muted); }
  .nokill { top: 712px; left: 520px; width: 385px; text-align: center; font-size: 14px; line-height: 23px; color: var(--muted); }
  .excuses { top: 788px; font-family: "Montserrat", Arial, sans-serif; font-weight: 800; font-size: 30px; letter-spacing: 2px; }
  .btn-primary { left: 642px; top: 846px; width: 140px; height: 44px; border-radius: 22px; background: var(--orange); color: var(--white);
    font-family: "Montserrat", Arial, sans-serif; font-weight: 700; font-size: 13px; letter-spacing: 2px; display: flex; align-items: center; justify-content: center; }
  .rule-2 { top: 920px; width: 60px; background: var(--line); }
  .notready { top: 940px; left: 520px; width: 385px; text-align: center; font-size: 14px; line-height: 24px; color: var(--muted); }
  .notready strong { color: var(--white); font-weight: 600; }

  .section-title { font-family: "Montserrat", Arial, sans-serif; font-weight: 800; color: var(--white); line-height: 1.05; letter-spacing: 1px; }
  .book-title { left: 60px; top: 552px; font-size: 32px; }
  .book-text { left: 62px; top: 636px; width: 230px; font-size: 13px; line-height: 21px; color: #fff3ea; }
  .btn-outline { width: 124px; height: 38px; border: 1.5px solid var(--white); border-radius: 19px; display: flex; align-items: center; justify-content: center;
    font-family: "Montserrat", Arial, sans-serif; font-weight: 700; font-size: 12px; letter-spacing: 2px; color: var(--white); }
  .btn-book { left: 62px; top: 724px; }
  .book-cover { left: 318px; top: 538px; width: 122px; height: 218px; background: linear-gradient(160deg, #6b4a38, #3a2218 60%, #1a0f0a);
    box-shadow: 0 10px 28px rgba(0,0,0,.45); border-right: 5px solid #0c0c0c; }

  .athlete { left: 0; top: 830px; width: 200px; height: 314px;
    background: linear-gradient(180deg, rgba(60,30,20,0) 0%, rgba(60,30,20,.55) 45%, rgba(40,20,14,.75) 100%); }
  .tips-title { left: 222px; top: 948px; font-size: 28px; }
  .tips-text { left: 224px; top: 990px; width: 225px; font-size: 13px; line-height: 21px; color: #fff3ea; }
  .btn-tips { left: 224px; top: 1076px; }

  .footer { left: 0; top: 1144px; width: 950px; height: 56px; background: var(--footer); display: flex; align-items: center; justify-content: center;
    font-size: 12px; letter-spacing: .5px; color: var(--muted); }
</style>
</head>
<body>
<main class="page">
  <svg class="backdrop" viewBox="0 0 950 1144" aria-hidden="true">
    <defs>
      <linearGradient id="warm" x1="0" y1="0" x2="0" y2="1">
        <stop offset="0" stop-color="#ee6a16"/>
        <stop offset="1" stop-color="#c94d0b"/>
      </linearGradient>
    </defs>
    <rect x="0" y="0" width="475" height="1144" fill="url(#warm)"/>
    <polygon points="0,0 475,0 475,470" fill="#f27a28" opacity=".55"/>
    <polygon points="0,470 475,830 475,1144 0,1144" fill="#a8400a" opacity=".35"/>
    <rect x="475" y="0" width="475" height="1144" fill="#141414"/>
    <polygon points="475,0 950,0 950,60 712,520" fill="#1a1a1a"/>
    <polygon points="475,860 712,620 950,1144 475,1144" fill="#171717"/>
  </svg>
  <div class="abs hero-photo" role="img" aria-label="Photo of an athlete training with weights, tinted orange"></div>

  <h1 class="abs brand brand-main">QUICK TICK</h1>
  <div class="abs brand brand-sub">QUEST</div>
  <div class="abs brand-rule"></div>

  <p class="abs col eyebrow">BORN 1960 – 1975?</p>
  <h2 class="abs col headline">FELLAS PAST FIFTY</h2>
  <div class="abs col subhead">OUT OF SHAPE &amp; OVERWEIGHT</div>
  <div class="abs rule rule-1"></div>
  <p class="abs intro">Discover The Quick Tick Quest plus dozens of insanely simple steps to get you in shape before your health deteriorates, you develop diabetes, have a stroke &amp; die way too early.</p>
  <p class="abs col goal">Our Goal is to Get You Healthy.</p>
  <p class="abs col secret">Wanna Know Our Secret?</p>
  <p class="abs col starts">It starts with</p>
  <p class="abs col quest">The Quick Tick Quest</p>
  <p class="abs col last">Think You Can Last a Full 10 Seconds?</p>
  <p class="abs col upfor">Are you up for it?</p>
  <p class="abs nokill">You don’t need to kill yourself with exercise, and you don’t need to starve on an extreme diet.</p>
  <h2 class="abs col excuses">NO MORE EXCUSES</h2>
  <a class="abs btn-primary">BUY HERE</a>
  <div class="abs rule rule-2"></div>
  <p class="abs notready"><strong>Not ready for the Quick Tick Quest yet?</strong><br>Text HELP to 40404 for free tips that make a real difference in your health and get you back in gear.</p>

  <h2 class="abs section-title book-title">THE<br>BOOK</h2>
  <p class="abs book-text">Ten seconds a day for thirty days. One small habit that finally sticks, then grows.</p>
  <a class="abs btn-outline btn-book">BUY NOW</a>
  <div class="abs book-cover" role="img" aria-label="Book cover of the Quick Tick Quest with a gym photo"></div>

  <div class="abs athlete" role="img" aria-label="Photo of a fit athlete holding dumbbells"></div>
  <h2 class="abs section-title tips-title">FREE TIPS</h2>
  <p class="abs tips-text">Short, no-nonsense texts that nudge you off the couch and into motion.</p>
  <a class="abs btn-outline btn-tips">GET TIPS</a>

  <footer class="abs footer">© 2020 Quick Tick Quest. All Rights Reserved.</footer>
</main>
</body>
</html>
```